Project Sign for Construction Company

Site contractor needs a 4'x8' sign to place on construction sites for advertising. Our company builds the infrastructure for new housing developments. These sign will be posted on the road side to be viewed by passing cars. I want a clean and bold look and feel that resembles my company logo.

Font styles to use
Other font styles liked:
• Hypatia Sans Pro

Colors

Designer to choose colors to be used in the design.

Requirements
Must have
• 555-382-9146 | Info@MarlowPaving.example
• CUC 8047319
• www.MarlowPaving.example
• Services
• Road Construction
• Site Preparation & Excavation
• Underground Utilities
• Shoreline Restoration
Nice to have
• Now Hiring
• Pipe Layers
• Foremen
• Equipment Operators
Should not have
• Should not have stock picture images used in the design, focus on logo and geometric shapes

```html
<!DOCTYPE html>
<html lang="en">
<head>
<meta charset="utf-8">
<title>Marlow Paving – Site Sign</title>
<link rel="stylesheet" href="https://fonts.googleapis.com/css2?family=Bebas+Neue&family=Arimo&display=swap">
<style>
  :root {
    --brand-blue: #04519c;
    --ink: #2b2321;
    --paper: #ffffff;
    --backdrop: #eeeeee;
  }
  html, body {
    margin: 0;
    padding: 0;
    width: 1200px;
    height: 1200px;
    overflow: hidden;
    background: var(--backdrop);
  }
  .canvas {
    position: relative;
    width: 1200px;
    height: 1200px;
  }
  .sign {
    position: absolute;
    left: 88px;
    top: 343px;
    width: 1024px;
    height: 513px;
    background: var(--paper);
    font-family: "Bebas Neue", "Arial Narrow", sans-serif;
  }
  .hiring-panel {
    position: absolute;
    left: 0;
    top: 0;
    width: 1024px;
    height: 513px;
  }
  .brand {
    position: absolute;
    left: 22px;
    top: 28px;
    width: 183px;
    display: flex;
    flex-direction: column;
    align-items: center;
    gap: 14px;
  }
  .brand-mark {
    width: 92px;
    height: 92px;
    border-radius: 50%;
    background: var(--brand-blue);
  }
  .brand-name {
    color: var(--brand-blue);
    font-size: 48px;
    line-height: 0.9;
    text-align: center;
    letter-spacing: 1px;
  }
  .services-label {
    position: absolute;
    left: 15px;
    top: 240px;
    width: 245px;
    height: 44px;
    background: var(--brand-blue);
    color: var(--paper);
    font-size: 34px;
    line-height: 46px;
    text-align: center;
  }
  .services-list {
    position: absolute;
    left: 25px;
    top: 290px;
    margin: 0;
    padding: 0;
    list-style: none;
    color: var(--ink);
    font-size: 36px;
    line-height: 1;
  }
  .services-list li {
    display: flex;
    align-items: center;
    gap: 8px;
    height: 33px;
    margin-bottom: 1px;
  }
  .services-list li:last-child { margin-top: 4px; }
  .tick { width: 15px; height: 14px; flex: none; }
  .hiring-title {
    position: absolute;
    left: 612px;
    top: 122px;
    margin: 0;
    color: var(--paper);
    font-weight: 400;
    font-size: 88px;
    line-height: 1;
    word-spacing: 14px;
    white-space: nowrap;
  }
  .roles {
    position: absolute;
    left: 681px;
    top: 198px;
    margin: 0;
    padding: 0;
    list-style: none;
    color: var(--paper);
    font-size: 46px;
    line-height: 1;
  }
  .roles li { height: 47px; }
  .roles li:last-child { margin-top: 5px; }
  .contact-bar {
    position: absolute;
    left: 0;
    bottom: 0;
    width: 1024px;
    height: 50px;
    background: var(--brand-blue);
    color: var(--paper);
    font-family: "Arimo", Arial, sans-serif;
    font-size: 24px;
    line-height: 50px;
    text-align: center;
    white-space: nowrap;
  }
</style>
</head>
<body>
<div class="canvas">
  <div class="sign">
    <svg class="hiring-panel" viewBox="0 0 1024 513" aria-hidden="true">
      <polygon points="529,17 1024,17 1024,447 529,447 572,231" fill="var(--brand-blue)"/>
    </svg>

    <div class="brand">
      <div class="brand-mark"></div>
      <div class="brand-name">MARLOW PAVING</div>
    </div>

    <div class="services-label">SERVICES</div>
    <ul class="services-list">
      <li><svg class="tick" viewBox="0 0 15 14"><rect x="1" y="3" width="10" height="10" fill="none" stroke="var(--brand-blue)" stroke-width="2"/><path d="M3.5 7.5l2.5 2.5 7-8" fill="none" stroke="var(--brand-blue)" stroke-width="2"/></svg>ROAD CONSTRUCTION</li>
      <li><svg class="tick" viewBox="0 0 15 14"><rect x="1" y="3" width="10" height="10" fill="none" stroke="var(--brand-blue)" stroke-width="2"/><path d="M3.5 7.5l2.5 2.5 7-8" fill="none" stroke="var(--brand-blue)" stroke-width="2"/></svg>SITE PREPARATION &amp; EXCAVATION</li>
      <li><svg class="tick" viewBox="0 0 15 14"><rect x="1" y="3" width="10" height="10" fill="none" stroke="var(--brand-blue)" stroke-width="2"/><path d="M3.5 7.5l2.5 2.5 7-8" fill="none" stroke="var(--brand-blue)" stroke-width="2"/></svg>UNDERGROUND UTILITIES</li>
      <li><svg class="tick" viewBox="0 0 15 14"><rect x="1" y="3" width="10" height="10" fill="none" stroke="var(--brand-blue)" stroke-width="2"/><path d="M3.5 7.5l2.5 2.5 7-8" fill="none" stroke="var(--brand-blue)" stroke-width="2"/></svg>SHORELINE RESTORATION</li>
    </ul>

    <h1 class="hiring-title">NOW HIRING</h1>
    <ul class="roles">
      <li>PIPE LAYERS</li>
      <li>FOREMEN</li>
      <li>EQUIPMENT OPERATORS</li>
    </ul>

    <div class="contact-bar">555-382-9146 | Info@MarlowPaving.example | CUC 8047319 | www.MarlowPaving.example</div>
  </div>
</div>
</body>
</html>
```